The Odette (wine label)

We are creating a new wine label for our vineyard in Tasmania, Australia.
This wine is dedicated to a very special person and needs to reflect elegance, beauty and longevity. We are looking for a wine label that incorporates the artwork on the attached photo (serpent tattoo).
We are calling the wine "The Odette" and it is a Pinot Noir (red wine). It is a light bodied but elegant wine, which reflects the person that it is named after.
The wine will be a 2024 Vintage Pinot Noir.

```html
<!DOCTYPE html>
<html lang="en">
<head>
<meta charset="utf-8">
<title>The Odette — Pinot Noir 2024 Label</title>
<link href="https://fonts.googleapis.com/css2?family=Playfair+Display:wght@400;700;900&family=Montserrat:wght@500;600;700&display=swap" rel="stylesheet">
<style>
  :root {
    --backdrop: #cfcfcf;
    --label-black: #030303;
    --arch-grey: #6e6f72;
    --ivory: #ffffff;
    --gold-deep: #8a5a1e;
    --gold-light: #f2c76c;
  }
  html, body {
    margin: 0;
    padding: 0;
    width: 1200px;
    height: 1117px;
    overflow: hidden;
    background: var(--backdrop);
  }
  .canvas {
    position: relative;
    width: 1200px;
    height: 1117px;
  }
  .wine-label {
    position: absolute;
    left: 134px;
    top: 16px;
    width: 931px;
    height: 1085px;
    display: block;
  }
  .label-ground { fill: var(--label-black); }
  .ornament-band { fill: url(#ornamentTone); }
  .arch-line { fill: none; stroke: var(--arch-grey); stroke-width: 6; }
  .serpent-art { fill: url(#serpentTone); }
  .wordmark {
    font-family: "Playfair Display", serif;
    font-weight: 700;
    font-size: 116px;
    fill: var(--ivory);
  }
  .varietal {
    font-family: "Playfair Display", serif;
    font-weight: 700;
    font-size: 54px;
    letter-spacing: 1px;
    fill: url(#goldFoil);
  }
  .gold-rule { fill: url(#goldFoil); }
  .vintage-tag {
    font-family: "Playfair Display", serif;
    font-weight: 700;
    font-size: 20px;
    letter-spacing: 10px;
    fill: var(--ivory);
  }
  .origin-line {
    font-family: "Montserrat", sans-serif;
    font-weight: 600;
    font-size: 18px;
    letter-spacing: 1.6px;
    fill: var(--ivory);
  }
  .vintage-year {
    font-family: "Montserrat", sans-serif;
    font-weight: 700;
    font-size: 36px;
    letter-spacing: 6px;
    fill: var(--ivory);
  }
</style>
</head>
<body>
<main class="canvas">
  <svg class="wine-label" viewBox="0 0 673 784" xmlns="http://www.w3.org/2000/svg" aria-label="The Odette Pinot Noir 2024 wine label">
    <defs>
      <linearGradient id="goldFoil" x1="0" y1="0" x2="1" y2="0">
        <stop offset="0" stop-color="var(--gold-deep)"/>
        <stop offset="0.45" stop-color="var(--gold-light)"/>
        <stop offset="1" stop-color="#a8722a"/>
      </linearGradient>
      <linearGradient id="ornamentTone" x1="0" y1="0" x2="0" y2="1">
        <stop offset="0" stop-color="#4a4b4e"/>
        <stop offset="1" stop-color="#1c1c1e"/>
      </linearGradient>
      <radialGradient id="serpentTone" cx="0.5" cy="0.5" r="0.6">
        <stop offset="0" stop-color="#8d8d8d"/>
        <stop offset="1" stop-color="#2a2a2a"/>
      </radialGradient>
      <clipPath id="labelEdge"><rect width="673" height="784"/></clipPath>
    </defs>

    <rect class="label-ground" width="673" height="784"/>

    <g clip-path="url(#labelEdge)">
      <path class="ornament-band" role="img" aria-label="Tribal scroll ornament framing the top of the label"
            d="M0 0 H673 V291 A396 396 0 0 0 0 291 Z"/>
      <circle class="arch-line" cx="336.5" cy="500" r="396"/>
    </g>

    <ellipse class="serpent-art" role="img" aria-label="Serpent tattoo artwork with tribal patterning, coiled and rising"
             cx="333" cy="214" rx="180" ry="145"/>

    <text class="wordmark" x="336.5" y="466" text-anchor="middle">ODETTE</text>

    <path class="gold-rule" d="M83 532 L150 528 L150 536 Z"/>
    <path class="gold-rule" d="M590 532 L523 528 L523 536 Z"/>
    <text class="varietal" x="336.5" y="551" text-anchor="middle">PINOT NOIR</text>

    <text class="vintage-tag" x="341.5" y="587" text-anchor="middle">VINTAGE</text>

    <text class="origin-line" x="336.5" y="644" text-anchor="middle">VINEYARD IN TASMANIA, AUSTRALIA</text>

    <text class="vintage-year" x="339.5" y="714" text-anchor="middle">2024</text>
  </svg>
</main>
</body>
</html>
```